Games for Classrooms Website Redesign

The purpose of the website redesign is to freshen up the content and update it to give a more modern look and feel. It will show what we do concisely and satisfy all potential visitors. We work with primary schools and the brand is fun.About: Games for Classrooms is a scheme that brings top Olympic athletes into primary schools to inspire children to do more physical activity. We typically run a half day event at the school where the athlete does a fun fitness circuit with the children and then an inspirational assembly with a demonstration and Q&A. The children are asked to collect sponsorship money to take part in the event and a large proportion of the money raised goes back to the school in the form of a voucher for them to spend on new sports equipment. 1. To generate more leads from potential customers/schools2. To engage the children and parents more in the event and get them excited for their upcoming visit whilst setting up a fundraiser page.3. To simplify and modernise what is already there.

I have attached some ideas for each of the pages (uploaded in brief)

Here is a link to our current website: www.gamesforclassrooms.org

I have also attached a link to the sponsorship form which shows the kind of look and feel we're after.

Target Market(s)

Primary school teachers
Primary school parents

Number of Pages Required

5+ page

Requirements
Must have
• Fun, modern.
• Be built on twitter bootstrap

```html
<!DOCTYPE html>
<html lang="en">
<head>
<meta charset="utf-8">
<title>Games for Classrooms – Home</title>
<link href="https://fonts.googleapis.com/css2?family=Montserrat:wght@600;700&family=Raleway:wght@300;400&family=Lato:wght@400;700&display=swap" rel="stylesheet">
<style>
:root{
  --ink:#222;
  --white:#fff;
  --muted:#cfcfcf;
  --green:#6cbf3c;
  --navy:#344559;
  --blue:#2c92dc;
  --red:#e0242f;
  --quote-bg:#ececec;
  --blog-bg:#0d2740;
  --footer:#333436;
  --footer-bottom:#2a2b2d;
  --navbar:#3a3b3d;
  --accent:#2fa54a;
}
*{margin:0;padding:0;box-sizing:border-box}
html,body{width:1200px;height:1200px;overflow:hidden;background:#fff}
body{font-family:'Lato',sans-serif;color:var(--ink);position:relative}
.page{position:absolute;left:392px;top:0;width:417px;height:1200px;overflow:hidden;box-shadow:0 0 40px rgba(0,0,0,.25);background:var(--footer)}
.section{position:absolute;left:0;width:417px;overflow:hidden}
.photo{position:absolute;inset:0}
.abs{position:absolute}
.hero{top:0;height:196px}
.hero .photo{background:linear-gradient(180deg,#6a4a35 0%,#8a6040 45%,#5a3e2a 100%)}
.hero-title{top:70px;left:0;width:417px;text-align:center;font-family:'Montserrat',sans-serif;font-weight:700;font-size:16px;color:var(--white);letter-spacing:.3px}
.hero-sub{top:96px;left:104px;width:210px;text-align:center;font-size:5.6px;line-height:9px;color:#eee}
.arrow{top:94px;color:#fff;font-size:9px}
.nav{left:0;width:417px;height:18px;display:flex;align-items:center}
.brand{position:absolute;left:58px;display:flex;align-items:center;gap:4px;font-family:'Montserrat',sans-serif;font-weight:700;color:var(--white)}
.brand .dot{width:9px;height:9px;border-radius:50%;background:var(--red)}
.menu{position:absolute;left:144px;display:flex;gap:8px;font-family:'Montserrat',sans-serif;font-weight:600;font-size:3.4px;color:var(--white);letter-spacing:.2px;text-transform:uppercase;align-items:center}
.nav-main{top:175px}
.nav-main .brand{font-size:5.4px;line-height:6px}
.sticky{top:196px;height:16px;background:var(--navbar)}
.sticky .brand{font-size:3.4px;line-height:4px}
.sticky .brand .dot{width:6px;height:6px}
.stats{top:212px;height:182px}
.stats .photo{background:radial-gradient(ellipse at 50% 30%,#9a9a9a 0%,#5e5e5e 55%,#3a3a3a 100%)}
.stat{top:52px;width:70px;text-align:center;color:var(--white)}
.stat svg{display:block;margin:0 auto 6px}
.stat .num{font-family:'Raleway',sans-serif;font-weight:300;font-size:12px}
.stat .rule{width:10px;height:1px;background:#fff;margin:4px auto 6px}
.stat .lbl{font-size:3.6px;text-transform:uppercase;letter-spacing:.3px}
.up{width:9px;height:9px;background:rgba(0,0,0,.45);right:5px;color:#fff;font-size:5px;text-align:center;line-height:9px}
.opp{top:394px;height:184px}
.opp .photo{background:linear-gradient(100deg,#4a3b3a 0%,#6a4f48 45%,#8a3a38 75%,#5a4a45 100%)}
.opp h2{top:56px;left:58px;width:150px;font-family:'Raleway',sans-serif;font-weight:300;font-size:15px;line-height:25px;color:var(--white)}
.opp p{top:113px;left:58px;width:180px;font-size:5px;line-height:9px;color:#eee}
.cards{top:578px;height:88px;display:flex}
.card{height:88px;padding:15px 10px 0 12px;color:var(--white)}
.card h3{font-family:'Montserrat',sans-serif;font-weight:600;font-size:6px;line-height:9px;text-transform:uppercase}
.card p{font-size:3.4px;line-height:6px;margin-top:7px;width:75px}
.btn{display:inline-block;border:1px solid var(--white);font-family:'Montserrat',sans-serif;font-weight:600;font-size:3.4px;padding:3px 7px;margin-top:6px;letter-spacing:.3px;text-transform:uppercase;color:var(--white)}
.green{width:102px;background:var(--green)}
.navy{width:106px;background:var(--navy)}
.blue{width:106px;background:var(--blue)}
.red{width:103px;background:var(--red)}
.quote{top:666px;height:42px;background:var(--quote-bg);text-align:center;font-family:'Montserrat',sans-serif;font-weight:700;font-size:7.2px;line-height:42px;color:#333;letter-spacing:.3px}
.what{top:708px;height:182px}
.what .photo{background:linear-gradient(180deg,#3e4a3c 0%,#5f6460 50%,#3c3c40 100%)}
.what h2{top:46px;left:246px;font-family:'Raleway',sans-serif;font-weight:300;font-size:16px;color:var(--white)}
.what p{top:78px;left:246px;width:110px;font-size:4.6px;line-height:9.6px;color:#eee}
.what .btn{position:absolute;top:140px;left:246px;margin:0}
.blog{top:890px;height:146px}
.blog .photo{background:radial-gradient(ellipse at 50% 100%,#1c4f77 0%,var(--blog-bg) 60%,#081c30 100%)}
.blog h2{top:38px;width:417px;text-align:center;font-family:'Raleway',sans-serif;font-weight:400;font-size:17px;color:var(--white)}
.blog p{top:72px;width:417px;text-align:center;font-size:5px;color:#ddd}
.blog .actions{top:93px;width:417px;display:flex;justify-content:center;gap:4px}
.blog .btn{margin:0}
.btn.solid{background:var(--white);color:var(--blog-bg)}
.footer{top:1036px;height:136px;background:var(--footer);color:#aaa;font-size:3.6px;line-height:6px}
.footer h4{font-family:'Montserrat',sans-serif;font-weight:600;font-size:4px;color:#ddd;letter-spacing:.4px;text-transform:uppercase;margin-bottom:7px}
.footer .brand{position:absolute;top:23px;left:58px;font-size:5.4px;line-height:6px;color:#777}
.footer b{color:#ddd}
.col-about{top:54px;left:58px;width:64px}
.col-menu{top:19px;left:126px;line-height:7.6px}
.col-articles{top:19px;left:194px;width:64px}
.col-articles .item{color:#ccc;margin-bottom:9px}
.col-articles .date{color:#777;display:block}
.col-news{top:20px;left:266px;width:100px}
.count{display:inline-block;width:48px}
.count .n{font-family:'Montserrat',sans-serif;font-weight:600;font-size:7px;color:#eee;line-height:10px}
.count .l{font-size:3.2px;text-transform:uppercase}
.signup{display:flex;margin-top:6px;height:9px}
.signup .field{width:68px;background:#222;color:#777;padding-left:4px;line-height:9px;font-size:3.4px}
.signup .go{width:25px;background:var(--accent);color:#fff;text-align:center;line-height:9px;font-size:3.6px}
.follow{display:flex;gap:18px;margin-top:10px}
.follow span{display:flex;align-items:center;gap:3px;font-size:3px;line-height:4px}
.follow i{width:10px;height:10px;display:block}
.bottom{top:1172px;height:28px;background:var(--footer-bottom);color:#777;font-size:3.2px;line-height:6px}
.bottom .left{top:8px;left:58px}
.bottom .icons{top:8px;left:276px;display:flex;gap:5px}
.bottom .icons i{width:4px;height:4px;border-radius:50%;background:#666;display:block}
.bottom .right{top:18px;left:242px}
</style>
</head>
<body>
<main class="page">

  <header class="section hero">
    <div class="photo" role="img" aria-label="Children doing push-ups in a school gym during a fitness circuit"></div>
    <div class="abs arrow" style="left:6px">&#8249;</div>
    <div class="abs arrow" style="right:6px">&#8250;</div>
    <h1 class="abs hero-title">EXERCISE FOR HEALTH</h1>
    <p class="abs hero-sub">Push-ups. Don't you love them? Actually, if you're a child doing the fitness circuits with a top athlete, the answer is a resounding yes! The only question is how many?</p>
    <nav class="abs nav nav-main">
      <div class="brand"><span class="dot"></span><span>Games<br>for Classrooms</span></div>
      <div class="menu"><span>Home</span><span>Athlete Visits</span><span>Get Active</span><span>Our Athletes</span><span>About Us</span><span>Contacts</span><span>Clubs</span>
        <svg width="5" height="5" viewBox="0 0 10 10"><circle cx="4" cy="4" r="3" fill="none" stroke="#fff" stroke-width="1.5"/><path d="M6 6l3 3" stroke="#fff" stroke-width="1.5"/></svg>
        <svg width="5" height="5" viewBox="0 0 10 10"><path d="M1 2h2l1 5h5l1-4H3.5" fill="none" stroke="#fff" stroke-width="1.2"/></svg>
      </div>
    </nav>
  </header>

  <nav class="section nav sticky">
    <div class="brand"><span class="dot"></span><span>Games<br>for Classrooms</span></div>
    <div class="menu"><span>Home</span><span>Athlete Visits</span><span>Get Active</span><span>Our Athletes</span><span>About Us</span><span>Contacts</span><span>Clubs</span>
      <svg width="5" height="5" viewBox="0 0 10 10"><circle cx="4" cy="4" r="3" fill="none" stroke="#fff" stroke-width="1.5"/><path d="M6 6l3 3" stroke="#fff" stroke-width="1.5"/></svg>
      <svg width="5" height="5" viewBox="0 0 10 10"><path d="M1 2h2l1 5h5l1-4H3.5" fill="none" stroke="#fff" stroke-width="1.2"/></svg>
    </div>
  </nav>

  <section class="section stats">
    <div class="photo" role="img" aria-label="Black and white photo of a smiling child with arms spread wide"></div>
    <div class="abs stat" style="left:58px">
      <svg width="12" height="12" viewBox="0 0 12 12"><circle cx="5" cy="4" r="2.5" fill="#fff"/><path d="M1 11c0-3 2-4.5 4-4.5s4 1.5 4 4.5z" fill="#fff"/></svg>
      <div class="num">1846+</div><div class="rule"></div><div class="lbl">People Envolved</div>
    </div>
    <div class="abs stat" style="left:135px">
      <svg width="12" height="12" viewBox="0 0 12 12"><circle cx="6" cy="5" r="3.5" fill="none" stroke="#fff"/><path d="M4.5 9h3v2h-3z" fill="#fff"/></svg>
      <div class="num">15360+</div><div class="rule"></div><div class="lbl">Young Pupils</div>
    </div>
    <div class="abs stat" style="left:212px">
      <svg width="12" height="12" viewBox="0 0 12 12"><rect x="1.5" y="2.5" width="9" height="8" fill="none" stroke="#fff"/><path d="M1.5 5h9M4 1v3M8 1v3" stroke="#fff"/></svg>
      <div class="num">326+</div><div class="rule"></div><div class="lbl">Wonderful Events</div>
    </div>
    <div class="abs stat" style="left:289px">
      <svg width="12" height="12" viewBox="0 0 12 12"><path d="M2 1v11" stroke="#fff"/><path d="M2 1.5h8l-2 2.5 2 2.5H2z" fill="#fff"/></svg>
      <div class="num">39+</div><div class="rule"></div><div class="lbl">Involved Organisations</div>
    </div>
    <div class="abs up" style="top:166px">&#708;</div>
  </section>

  <section class="section opp">
    <div class="photo" role="img" aria-label="Wheelchair rugby players competing in a crowded arena"></div>
    <h2 class="abs">Opportunity for Everybody</h2>
    <p class="abs">The Valour Games is an international sporting event for wounded, injured and sick servicemen and women.</p>
    <div class="abs up" style="top:168px">&#708;</div>
  </section>

  <section class="section cards">
    <article class="card green"><h3>Headteachers &amp; Principals</h3><p>How's this going to help your school and make a difference for the pupils?</p><span class="btn">Read More</span></article>
    <article class="card navy"><h3>PE Coordinator</h3><p>What's involved? How easy is it to have an athlete visit my school?</p><span class="btn">Read More</span></article>
    <article class="card blue"><h3>Parents</h3><p>Are you wondering what a Games for Classrooms event is all about?</p><span class="btn">Read More</span></article>
    <article class="card red"><h3>Pupils</h3><p>Who will we meet and what are we going to do?</p><span class="btn">Read More</span></article>
  </section>

  <section class="section quote">“WONDERFUL - THE FUNDS RAISED WILL HELP US IN THE PURCHASE OF NEW GYM EQUIPMENT”</section>

  <section class="section what">
    <div class="photo" role="img" aria-label="Pack of road cyclists racing through a city street"></div>
    <h2 class="abs">What We Do</h2>
    <p class="abs">Games for Classrooms encourage young people to live healthy lifestyles, challenge, surprise and excite them to do just that, giving every child the opportunity to join in and help their school thrive.</p>
    <span class="btn">Contact Us</span>
    <div class="abs up" style="top:166px">&#708;</div>
  </section>

  <section class="section blog">
    <div class="photo" role="img" aria-label="Dark blue underwater scene with a swimmer"></div>
    <h2 class="abs">Latest Article from Blog</h2>
    <p class="abs">A short description about the blog post with a read more button.</p>
    <div class="abs actions"><span class="btn">Read More</span><span class="btn solid">Blog</span></div>
  </section>

  <footer class="section footer">
    <div class="brand"><span class="dot" style="background:#555"></span><span>Games<br>for Classrooms</span></div>
    <div class="abs col-about">
      <p>Games for Classrooms. Athletes who Inspire Kids.</p><br>
      <p><b>Headquarters:</b><br>12 Orchard Yard, Fenwick Park, Norbridge NB4 7QT</p><br>
      <p><b>Phone:</b> (44) 01632 960 418<br><b>Fax:</b> 01 555 0192 (Ireland)<br><b>Email:</b> hello@gamesforclassrooms.org</p>
    </div>
    <div class="abs col-menu">
      <h4>Menu</h4>
      <p>Athletes Visits<br>The Event<br>Get Active<br>Our Athletes<br>About us<br>Contacts<br>Clubs</p>
    </div>
    <div class="abs col-articles">
      <h4>Recent Articles</h4>
      <p class="item">Lorem ipsum dolor sit amet, consectetur<span class="date">10th Jan 2016</span></p>
      <p class="item">Elit Assumenda vel amet dolorum quasi<span class="date">12th Dec 2015</span></p>
      <p class="item">Debitis nihil placeat, illum est nisi<span class="date">10th July 2015</span></p>
    </div>
    <div class="abs col-news">
      <div><span class="count"><span class="n">1,506</span><br><span class="l">App Downloads</span></span><span class="count"><span class="n">18,465</span><br><span class="l">Clients</span></span></div>
      <p style="margin-top:12px;color:#ccc">Subscribe to Our Newsletter to get Important News, Amazing Offers &amp; Event Dates:</p>
      <div class="signup"><span class="field">Enter your Email</span><span class="go">Subscribe</span></div>
      <div class="follow">
        <span><i style="background:#3b5a98"></i>Like us<br>on our page</span>
        <span><i style="background:#f0772a"></i>Subscribe<br>to our Feed</span>
      </div>
    </div>
  </footer>

  <div class="section bottom">
    <p class="abs left">Copyright © 2016 All Rights Reserved by Games for Classrooms<br>Terms of Use / Privacy Policy</p>
    <div class="abs icons"><i></i><i></i><i></i><i></i><i></i><i></i><i></i><i></i></div>
    <p class="abs right">hello@gamesforclassrooms.org · (44) 01632 960 418</p>
    <div class="abs up" style="top:16px;background:#444">&#708;</div>
  </div>

</main>
</body>
</html>
```